Real Estate Business Cards

Looking for a clean, sharp and professional look for our Real Estate investment Fund that invests in Multi Family Apartment buildings.

Target Market(s)

Real Estate Fund

Industry/Entity Type

Real Estate

Contact Information for Business Card

Company Description: Real Estate Investment Fund
Company Name: RKW Holdings
Name: Marcus Olvane
Cell: (917) 482-0657
Email: marcus@rkwholdings-example.com
Website: www.rkwholdings-example.com
Address: 418, 9th Street, Brooklyn NY 11218

Colors

Designer to choose colors to be used in the design.

Requirements
Nice to have
• Colors to match logo

```html
<!DOCTYPE html>
<html lang="en">
<head>
<meta charset="utf-8">
<title>RKW Holdings – Business Card</title>
<link rel="stylesheet" href="https://fonts.googleapis.com/css2?family=Cinzel:wght@400;500&family=Lato:wght@400&display=swap">
<style>
  :root {
    --brand-blue: #1172aa;
    --card-white: #f4f4f4;
    --ink-grey: #3f4246;
    --divider: #d6d6d6;
    --backdrop: #e4e5e7;
  }
  * { box-sizing: border-box; margin: 0; padding: 0; }
  html, body {
    width: 1200px;
    height: 1015px;
    overflow: hidden;
    background: var(--backdrop);
  }
  .sheet {
    position: relative;
    width: 1200px;
    height: 1015px;
  }
  .card {
    position: absolute;
    left: 240px;
    width: 720px;
    height: 412px;
    box-shadow: 0 10px 28px rgba(0, 0, 0, 0.22);
    overflow: hidden;
  }
  /* Front */
  .card-front {
    top: 70px;
    background: var(--brand-blue);
    display: flex;
    align-items: center;
    justify-content: center;
    gap: 28px;
  }
  .brand-mark {
    width: 74px;
    height: 74px;
    flex: none;
  }
  .card-front .brand-mark { background: #ffffff; }
  .brand-name {
    font-family: "Cinzel", serif;
    font-weight: 400;
    font-size: 40px;
    letter-spacing: 2px;
    white-space: nowrap;
  }
  .card-front .brand-name { color: #ffffff; }

  /* Back */
  .card-back {
    top: 532px;
    background: var(--card-white);
  }
  .card-back .base-band {
    position: absolute;
    left: 0; right: 0; bottom: 0;
    height: 14px;
    background: var(--brand-blue);
  }
  .card-back .brand-block {
    position: absolute;
    left: 0; top: 0;
    width: 380px;
    height: 398px;
    display: flex;
    flex-direction: column;
    align-items: center;
    justify-content: center;
    gap: 26px;
    padding-top: 40px;
  }
  .card-back .brand-mark { width: 64px; height: 64px; background: var(--brand-blue); }
  .card-back .brand-name { color: var(--brand-blue); font-size: 34px; }
  .card-back .divider {
    position: absolute;
    left: 380px;
    top: 30px;
    width: 1px;
    height: 330px;
    background: var(--divider);
  }
  .contact {
    position: absolute;
    left: 420px;
    top: 96px;
    font-family: "Lato", sans-serif;
    color: var(--ink-grey);
    font-size: 15.5px;
    line-height: 1.5;
  }
  .contact .person {
    font-family: "Cinzel", serif;
    font-weight: 500;
    color: var(--brand-blue);
    font-size: 23px;
    letter-spacing: 0.5px;
    margin-bottom: 6px;
  }
  .contact-line {
    display: flex;
    align-items: center;
    gap: 8px;
    white-space: nowrap;
  }
  .contact-line svg { width: 13px; height: 13px; flex: none; fill: var(--brand-blue); }
  .address { margin-top: 14px; }
</style>
</head>
<body>
<main class="sheet">
  <section class="card card-front" aria-label="Card front">
    <span class="brand-mark" aria-hidden="true"></span>
    <span class="brand-name">RKW Holdings</span>
  </section>

  <section class="card card-back" aria-label="Card back">
    <div class="brand-block">
      <span class="brand-mark" aria-hidden="true"></span>
      <span class="brand-name">RKW Holdings</span>
    </div>
    <span class="divider" aria-hidden="true"></span>
    <div class="contact">
      <p class="person">Marcus Olvane</p>
      <p class="contact-line">
        <svg viewBox="0 0 16 16" aria-hidden="true"><path d="M3.6 1.2l2.3 2.7-1.4 1.8c.9 2 2.5 3.8 4.6 4.9l1.8-1.4 2.8 2.3-1.6 2.7C6.7 14.2 1.6 9.1 1 3z"/></svg>
        (917) 482-0657
      </p>
      <p class="contact-line">
        <svg viewBox="0 0 16 16" aria-hidden="true"><path d="M1 3h14v10H1z M1.8 3.8L8 8.6l6.2-4.8" /><path d="M1 3l7 5.4L15 3z" fill="#ffffff"/></svg>
        marcus@rkwholdings-example.com
      </p>
      <p class="contact-line">
        <svg viewBox="0 0 16 16" aria-hidden="true"><circle cx="8" cy="8" r="7"/><path d="M1.5 8h13M8 1c2.2 2 2.2 12 0 14M8 1c-2.2 2-2.2 12 0 14" stroke="#ffffff" stroke-width="1" fill="none"/></svg>
        www.rkwholdings-example.com
      </p>
      <p class="address">418, 9th Street<br>Brooklyn NY 11218</p>
    </div>
    <span class="base-band" aria-hidden="true"></span>
  </section>
</main>
</body>
</html>
```